Two Versions of a Business Card for a Lawyer

Summary: I need a logo and a business card. The business card is two-sided and comes in two versions. One version is conservative, the other is slightly different with one or more pink embellishments in the logo or somewhere else in the business card.
I'm about to start off as a sole practitioner in criminal and immigration law. I'll largely be working with marginalised communities and in areas of social justice. One of my main focuses will be gendered violence, I'm hoping to specialise my practice towards representing victims of domestic and sexual violence and sex workers. I want a business card which would attract this clientele and make them feel safe to speak with me. I'd also like it to communicate a sense of hope.
However, the business card still has to be very conservative as the legal profession is very stuffy. So I was thinking of having two versions of the same card, one would be very straight forward while the other would have a **pink embellishment** or perhaps several. For example, if the scales of justice were used in the design, maybe the second version would have a pink flower about to bloom on the scale somewhere. Or maybe it's my logo that is different and pink.
While both designs have to be pretty conservative, I still want it to give off a sense that I'm alternative and think outside the box. With lawyers, I think a little bit of deviation goes a long way (less is more).
As far as colour goes (other than the pink embellishment), I was thinking something monochromatic, probably black and white but I am open to considering more colours. I personally love colour, and would love to use more colour, but am hesitant because of the nature of the profession. If you can find a way to use more colour while keeping it conservative and letting the pink pop, I'd be pretty pleased.
In general, I would prefer a clean simplistic design and logo. It should be immediately obvious that I'm a lawyer just by glancing at the card. I'm open to symbols of law, like the scales of justice or lady justice or something else. However, I don't want it to be the same as everyone else's.
Eventually, the design/style should be easy to recreate in the form of a website.
As far as the logo goes, it would probably use a circle as my last name starts with the letter "O". It can be very simple, with just my name and "Barrister & Solicitor". I don't currently have a logo, but the winning designer will be invited to provide a separate file for just the logo for an additional fee (I think it was CA$99). (Please ignore the uploaded logo file, it just wouldn't let me continue without uploading something).
As for the information that should go into the card, I'm still finalizing my address and phone number. So please use a placeholder for now.
Target Market(s)
Women, victims of sexual or domestic violence, refugees, people in need of legal services
Industry/Entity Type
Lawyer
Contact Information for Business Card
Maren Vickery
Barrister & Solicitor
LL.B., B.C.L., B.F.A.
Criminal & Immigration Law
Street address
Toronto, ON
Postal Code
Phone number
Fax number
Email
Logo Text
Maren Vickery, Barrister & Solicitor
Requirements
Must have
- Two versions
- One with pink
- Simplistic
Nice to have
- Maybe more colour
Should not have
- Not too conservative
- Not too predictable

```html
<!DOCTYPE html>
<html lang="en">
<head>
<meta charset="utf-8">
<title>Maren Vickery — Business Cards</title>
<link rel="stylesheet" href="https://fonts.googleapis.com/css2?family=Cinzel:wght@700&family=Ubuntu:wght@400;500&display=swap">
<style>
  :root {
    --backdrop: #30373a;
    --paper: #ffffff;
    --pink: #ee33ee;
    --plum: #3b1141;
    --mauve: #7a4a8a;
    --slate: #4f5e5e;
    --coal: #111111;
    --graphite: #444b4b;
  }
  html, body { margin: 0; padding: 0; overflow: hidden; }
  body { background: var(--backdrop); }
  .sheet {
    position: relative; width: 831px; height: 1200px;
    background: var(--backdrop); overflow: hidden;
    font-family: "Ubuntu", sans-serif;
  }
  .card {
    position: absolute; width: 363px; height: 541px;
    background: var(--paper); overflow: hidden;
  }
  .card--pink { --band: var(--pink); --stripe: var(--plum); --ink: var(--plum); --soft: var(--mauve); --icon: var(--pink); --rule: #6e5a7e; --underline: var(--pink); }
  .card--mono { --band: var(--slate); --stripe: var(--coal); --ink: var(--coal); --soft: var(--graphite); --icon: var(--slate); --rule: var(--pink); --underline: var(--pink); }

  .pos-front-a { left: 31px; top: 31px; }
  .pos-back-a  { left: 438px; top: 31px; width: 362px; }
  .pos-front-b { left: 31px; top: 626px; }
  .pos-back-b  { left: 438px; top: 626px; width: 362px; }

  .band, .stripe { position: absolute; left: 0; right: 0; }
  .band { background: var(--band); }
  .stripe { background: var(--stripe); height: 10px; }
  .band--top { top: 0; height: 47px; }
  .stripe--top { top: 53px; }
  .stripe--bottom { top: 480px; }
  .band--bottom { top: 495px; height: 46px; }

  .emblem { position: absolute; border-radius: 50%; background: var(--ink); }
  .emblem--pink { background: var(--pink); }

  .wordmark {
    position: absolute; left: 0; right: 0; text-align: center;
    font-family: "Cinzel", serif; font-weight: 700; color: var(--ink);
    line-height: 1; white-space: nowrap;
  }
  .wordmark-rule { position: absolute; height: 2px; background: var(--underline); }
  .wordmark-tag {
    position: absolute; left: 0; right: 0; text-align: center;
    font-weight: 500; color: var(--soft); letter-spacing: 2px; line-height: 1;
  }

  .front-a .emblem { left: 125px; top: 177px; width: 112px; height: 112px; }
  .front-a .wordmark { top: 312px; font-size: 26px; letter-spacing: 1px; }
  .front-a .wordmark-rule { left: 65px; width: 233px; top: 340px; }
  .front-a .wordmark-tag { top: 350px; font-size: 14px; }

  .front-b .emblem { left: 112px; top: 152px; width: 140px; height: 140px; }
  .front-b .wordmark { top: 320px; font-size: 32px; letter-spacing: 1px; }
  .front-b .wordmark-rule { left: 38px; width: 288px; top: 357px; }
  .front-b .wordmark-tag { top: 368px; font-size: 15px; letter-spacing: 2.5px; }

  .holder-name {
    position: absolute; left: 26px; top: 95px; margin: 0;
    font-family: "Cinzel", serif; font-weight: 700; font-size: 31px;
    color: var(--ink); line-height: 1; white-space: nowrap; letter-spacing: 0.5px;
  }
  .practice {
    position: absolute; left: 26px; top: 137px; margin: 0;
    font-size: 20px; font-weight: 500; color: var(--ink);
    letter-spacing: 1.2px; line-height: 1; white-space: nowrap;
  }
  .degrees {
    position: absolute; left: 0; right: 0; top: 177px; margin: 0;
    text-align: center; font-size: 13px; color: var(--ink); line-height: 1;
  }
  .divider { position: absolute; left: 26px; width: 310px; top: 223px; height: 2px; background: var(--rule); }

  .contact { position: absolute; left: 0; right: 0; text-align: center; font-size: 15px; color: var(--ink); line-height: 21px; margin: 0; }
  .contact--address { top: 252px; }
  .contact--phone { top: 313px; }
  .contact--fax { top: 351px; }
  .contact--email { top: 388px; }

  .icon { position: absolute; left: 29px; width: 28px; height: 26px; color: var(--icon); }
  .icon--mail { top: 250px; }
  .icon--chat { top: 306px; }
  .icon--fax { top: 344px; }
  .icon--at { top: 382px; }

  .seal {
    position: absolute; left: 131px; top: 416px; width: 96px; height: 96px;
    border-radius: 50%; border: 3px solid var(--paper); box-sizing: content-box;
    background: var(--ink); z-index: 2;
  }
  .seal--pink { background: var(--pink); }
</style>
</head>
<body>
<div class="sheet">

  <!-- Pink edition, front -->
  <section class="card card--pink front-a pos-front-a">
    <div class="band band--top"></div><div class="stripe stripe--top"></div>
    <div class="emblem emblem--pink"></div>
    <div class="wordmark">MAREN VICKERY</div>
    <div class="wordmark-rule"></div>
    <div class="wordmark-tag">Barrister &amp; Solicitor</div>
    <div class="stripe stripe--bottom"></div><div class="band band--bottom"></div>
  </section>

  <!-- Pink edition, back -->
  <section class="card card--pink pos-back-a">
    <div class="band band--top"></div><div class="stripe stripe--top"></div>
    <h1 class="holder-name">MAREN VICKERY</h1>
    <p class="practice">Criminal &amp; Immigration Law</p>
    <p class="degrees">LL.B., B.C.L., B.F.A.</p>
    <div class="divider"></div>

    <svg class="icon icon--mail" viewBox="0 0 28 26"><rect x="2" y="4" width="24" height="18" fill="currentColor"/><path d="M2 4 L14 15 L26 4 M2 22 L11 12 M26 22 L17 12" stroke="#fff" stroke-width="1.6" fill="none"/></svg>
    <p class="contact contact--address">Street address, Toronto, ON<br>Postal Code</p>

    <svg class="icon icon--chat" viewBox="0 0 28 26" fill="none" stroke="currentColor" stroke-width="1.5"><path d="M3 4 h13 a2 2 0 0 1 2 2 v7 a2 2 0 0 1 -2 2 h-8 l-4 3 v-3 a2 2 0 0 1 -3 -2 v-7 a2 2 0 0 1 2 -2z"/><path d="M19 9 h5 a2 2 0 0 1 2 2 v7 a2 2 0 0 1 -2 2 v3 l-4 -3 h-7 a2 2 0 0 1 -2 -2 v-2"/><circle cx="17" cy="16" r="0.8" fill="currentColor"/><circle cx="20" cy="16" r="0.8" fill="currentColor"/><circle cx="23" cy="16" r="0.8" fill="currentColor"/></svg>
    <p class="contact contact--phone">+00 000 000 0000</p>

    <svg class="icon icon--fax" viewBox="0 0 28 26" fill="none" stroke="currentColor" stroke-width="1.5"><rect x="7" y="2" width="14" height="8"/><rect x="3" y="9" width="22" height="12" rx="3"/><rect x="8" y="15" width="12" height="9" fill="#fff"/><path d="M10 18h8M10 21h8"/></svg>
    <p class="contact contact--fax">+00 000 000 0000</p>

    <svg class="icon icon--at" viewBox="0 0 28 26"><text x="14" y="21" text-anchor="middle" font-family="Ubuntu, sans-serif" font-size="26" fill="currentColor">@</text></svg>
    <p class="contact contact--email">maren@maren-vickery.com</p>

    <div class="seal seal--pink"></div>
    <div class="stripe stripe--bottom"></div><div class="band band--bottom"></div>
  </section>

  <!-- Conservative edition, front -->
  <section class="card card--mono front-b pos-front-b">
    <div class="band band--top"></div><div class="stripe stripe--top"></div>
    <div class="emblem"></div>
    <div class="wordmark">MAREN VICKERY</div>
    <div class="wordmark-rule"></div>
    <div class="wordmark-tag">Barrister &amp; Solicitor</div>
    <div class="stripe stripe--bottom"></div><div class="band band--bottom"></div>
  </section>

  <!-- Conservative edition, back -->
  <section class="card card--mono pos-back-b">
    <div class="band band--top"></div><div class="stripe stripe--top"></div>
    <h1 class="holder-name">MAREN VICKERY</h1>
    <p class="practice">Criminal &amp; Immigration Law</p>
    <p class="degrees">LL.B., B.C.L., B.F.A.</p>
    <div class="divider"></div>

    <svg class="icon icon--mail" viewBox="0 0 28 26"><rect x="2" y="4" width="24" height="18" fill="currentColor"/><path d="M2 4 L14 15 L26 4 M2 22 L11 12 M26 22 L17 12" stroke="#fff" stroke-width="1.6" fill="none"/></svg>
    <p class="contact contact--address">Street address, Toronto, ON<br>Postal Code</p>

    <svg class="icon icon--chat" viewBox="0 0 28 26" fill="none" stroke="currentColor" stroke-width="1.5"><path d="M3 4 h13 a2 2 0 0 1 2 2 v7 a2 2 0 0 1 -2 2 h-8 l-4 3 v-3 a2 2 0 0 1 -3 -2 v-7 a2 2 0 0 1 2 -2z"/><path d="M19 9 h5 a2 2 0 0 1 2 2 v7 a2 2 0 0 1 -2 2 v3 l-4 -3 h-7 a2 2 0 0 1 -2 -2 v-2"/><circle cx="17" cy="16" r="0.8" fill="currentColor"/><circle cx="20" cy="16" r="0.8" fill="currentColor"/><circle cx="23" cy="16" r="0.8" fill="currentColor"/></svg>
    <p class="contact contact--phone">+00 000 000 0000</p>

    <svg class="icon icon--fax" viewBox="0 0 28 26" fill="none" stroke="currentColor" stroke-width="1.5"><rect x="7" y="2" width="14" height="8"/><rect x="3" y="9" width="22" height="12" rx="3"/><rect x="8" y="15" width="12" height="9" fill="#fff"/><path d="M10 18h8M10 21h8"/></svg>
    <p class="contact contact--fax">+00 000 000 0000</p>

    <svg class="icon icon--at" viewBox="0 0 28 26"><text x="14" y="21" text-anchor="middle" font-family="Ubuntu, sans-serif" font-size="26" fill="currentColor">@</text></svg>
    <p class="contact contact--email">maren@maren-vickery.com</p>

    <div class="seal"></div>
    <div class="stripe stripe--bottom"></div><div class="band band--bottom"></div>
  </section>

</div>
</body>
</html>
```